I need bigcommerce design template

hi, am looking for a quality, professional, attractive and mature bigcommerce template for my site. My site will sell clothes and bags and shoes. Basically what you are to do is setup the store. I have domain name which hostwren will attach them self.

It Professional

```html
<!DOCTYPE html>
<html lang="en">
<head>
<meta charset="utf-8">
<title>Storefront Template</title>
<link href="https://fonts.googleapis.com/css2?family=Open+Sans:wght@400;600;700&display=swap" rel="stylesheet">
<style>
:root{
  --red:#a3141b;
  --red-dark:#7d0d12;
  --red-mid:#b5181f;
  --red-bright:#d0222a;
  --grey-bg:#ededed;
  --grey-line:#d6d6d6;
  --grey-text:#777;
  --text:#333;
  --white:#fff;
  --dark:#1f1f1f;
}
*{box-sizing:border-box;margin:0;padding:0}
html,body{width:1200px;height:2459px;overflow:hidden}
body{position:relative;background:var(--white);font-family:"Open Sans",Arial,sans-serif;color:var(--text)}
.abs{position:absolute}

/* top bar */
.top-bar{left:0;top:0;width:1200px;height:54px;background:var(--red-dark)}
.account-links{left:135px;top:0;height:54px;display:flex;align-items:center;gap:34px;color:var(--white);font-size:13px;font-weight:600}
.account-links span{display:flex;align-items:center;gap:7px}
.selector{top:6px;height:42px;background:var(--white);border-radius:3px;display:flex;align-items:center;gap:8px;padding:0 12px;font-size:12px;font-weight:700;color:var(--red)}
.lang{left:836px;width:110px}
.currency{left:954px;width:110px}

/* main nav */
.main-nav{left:0;top:54px;width:1200px;height:94px;background:linear-gradient(var(--red-mid),var(--red))}
.nav-links{left:135px;top:88px;display:flex;align-items:center;gap:0;font-size:11px;font-weight:700;color:var(--white);letter-spacing:.3px}
.nav-links span{padding:0 22px;border-left:1px solid rgba(255,255,255,.5);line-height:12px}
.nav-links span:first-child{border:none}
.nav-links .active{background:var(--white);color:var(--red);padding:8px 14px;border-radius:2px;margin-right:22px;border:none}
.nav-links .active + span{border-left:none}
.social-top{left:934px;top:90px;display:flex;gap:14px}
.social-top i{width:16px;height:16px;border-radius:50%;background:var(--white);display:block}

/* category bar */
.cat-bar{left:0;top:148px;width:1200px;height:68px;background:var(--grey-bg)}
.cat-links{left:130px;top:172px;display:flex;font-size:14px;font-weight:600;color:var(--red)}
.cat-links span{padding-right:36px}
.cat-links b{padding-right:36px;font-weight:400}
.search{left:873px;top:166px;width:194px;height:34px;border:2px solid var(--red);display:flex;background:var(--white)}
.search span{flex:1;font-size:11px;font-style:italic;color:var(--grey-text);display:flex;align-items:center;padding-left:46px}
.search i{width:32px;background:var(--red);display:flex;align-items:center;justify-content:center}

/* hero */
.hero-img{left:177px;top:258px;width:573px;height:276px;background:linear-gradient(120deg,#8c6a52,#c9b39c 45%,#6f8f54 70%,#b23a33)}
.slide-arrow{width:30px;height:36px;background:var(--red);display:flex;align-items:center;justify-content:center}
.dots{left:674px;top:558px;display:flex;gap:7px}
.dots i{width:10px;height:10px;border:1px solid #aaa;display:block}
.dots i.on{background:var(--red);border-color:var(--red)}
.perks{left:800px;top:216px;width:267px;height:399px;background:var(--red-bright)}
.perk{position:absolute;left:0;width:267px;text-align:center;color:var(--white)}
.perk h4{font-size:11px;font-weight:700;margin-top:6px}
.perk p{font-size:10px;line-height:14px;padding:0 40px}
.perk.dark{background:rgba(0,0,0,.12)}

/* collections */
.grey-area{left:0;top:615px;width:1200px;height:1426px;background:var(--grey-bg)}
.tag{left:130px;height:39px;width:190px;background:var(--red);color:var(--white);font-size:11px;font-weight:700;display:flex;align-items:center;padding-left:22px;clip-path:polygon(0 0,160px 0,190px 100%,0 100%)}
.panel{left:130px;width:937px;height:428px;background:var(--white);border:1px solid var(--grey-line)}
.thumb{width:152px;height:148px;border:5px solid #e8e8e8;background:var(--white);padding:6px}
.thumb.sel{border-color:var(--red)}
.thumb div{width:100%;height:100%}
.pointer{width:0;height:0;border-top:14px solid transparent;border-bottom:14px solid transparent;border-left:16px solid var(--red)}
.loadbar{display:flex;align-items:center;font-size:13px;font-weight:700;color:var(--red)}
.loadbar i{width:38px;height:38px;border-radius:50%;background:var(--red);display:block;margin-right:14px}
.radio{display:flex;align-items:center;gap:7px;font-size:12px;font-weight:400;color:#999}
.radio b{width:11px;height:11px;border-radius:50%;border:1px solid #bbb;display:block}
.radio.on{color:var(--red);font-weight:600}
.radio.on b{border-color:var(--red)}
.feature{width:372px;height:391px}
.price-bar{left:0;bottom:0;width:372px;height:91px;background:rgba(20,20,20,.75);color:var(--white)}
.price-bar .price{position:absolute;left:28px;top:32px;font-size:20px;font-weight:600}

/* latest */
.latest{left:130px;top:1660px;width:937px;height:356px;background:var(--white);border:1px solid var(--grey-line)}
.tabs{left:421px;top:1689px;display:flex}
.tabs span{width:108px;height:35px;border:1px solid var(--grey-line);font-size:11px;display:flex;align-items:center;justify-content:center;color:#999;margin-left:-1px}
.tabs span.on{border:2px solid var(--red);color:var(--red);font-weight:600}
.card{top:1753px;width:158px;height:227px}
.card .label{position:absolute;left:12px;top:62px;width:134px;height:102px;background:rgba(30,30,30,.75);color:var(--white);padding:20px 0 0 12px}
.card .label.red{background:rgba(206,52,36,.85)}
.card .label small{font-size:8px;font-weight:700;display:block}
.card .label em{font-style:normal;font-size:9px;letter-spacing:1px}
.card .label strong{position:absolute;right:10px;top:26px;font-size:22px;font-weight:600}

/* footer */
.foot-col h5{font-size:13px;font-weight:600;color:var(--red);letter-spacing:.3px;padding-bottom:8px;border-bottom:1px solid var(--red);display:inline-block;width:60px;white-space:nowrap}
.foot-col ul{list-style:none;margin-top:26px}
.foot-col li{font-size:10.5px;line-height:23.5px;color:#444}
.news-input{left:598px;top:2171px;width:184px;height:32px;border:1px solid var(--red);font-size:11px;display:flex;align-items:center;padding-left:24px}
.subscribe{left:598px;top:2215px;width:113px;height:32px;background:var(--red);color:var(--white);font-size:11px;font-weight:600;display:flex;align-items:center;justify-content:center}
.news-note{left:598px;top:2258px;width:160px;font-size:10.5px;line-height:18px;color:#444}
.addr-row{left:841px;display:flex;gap:16px;font-size:10.5px;line-height:16px;color:#444}
.addr-row i{width:24px;height:24px;border-radius:50%;background:var(--red);flex:none;display:block}
.addr-row span.em{color:var(--red);text-decoration:underline}
.social-foot{left:540px;top:2314px;display:flex;gap:18px}
.social-foot i{width:17px;height:17px;border-radius:50%;background:#333;display:block}
.copyright{left:0;top:2356px;width:1200px;text-align:center;font-size:10.5px;font-weight:600;color:#333}
</style>
</head>
<body>

<header>
  <div class="abs top-bar"></div>
  <nav class="abs account-links">
    <span><svg width="12" height="11" viewBox="0 0 12 11"><path d="M6 0 12 5H10V11H7V7H5V11H2V5H0Z" fill="#fff"/></svg>Home</span>
    <span><svg width="10" height="12" viewBox="0 0 10 12"><circle cx="5" cy="3" r="3" fill="#fff"/><path d="M0 12C0 7 10 7 10 12Z" fill="#fff"/></svg>My Account</span>
    <span><svg width="14" height="12" viewBox="0 0 14 12"><path d="M0 1H3L5 8H12L14 3H4" stroke="#fff" stroke-width="1.6" fill="none"/><circle cx="6" cy="10.5" r="1.3" fill="#fff"/><circle cx="11" cy="10.5" r="1.3" fill="#fff"/></svg>Shopping Cart</span>
    <span><svg width="12" height="10" viewBox="0 0 12 10"><path d="M1 5 4.5 8.5 11 1" stroke="#fff" stroke-width="2" fill="none"/></svg>Checkout</span>
  </nav>
  <div class="abs selector lang"><i style="width:18px;height:11px;background:#2b3f8c;display:block"></i>ENGLISH<svg width="9" height="6" viewBox="0 0 9 6"><path d="M1 1 4.5 5 8 1" stroke="#a3141b" stroke-width="1.6" fill="none"/></svg></div>
  <div class="abs selector currency"><i style="width:16px;height:16px;background:var(--red);color:#fff;font-style:normal;font-size:11px;display:flex;align-items:center;justify-content:center">$</i>DOLLER<svg width="9" height="6" viewBox="0 0 9 6"><path d="M1 1 4.5 5 8 1" stroke="#a3141b" stroke-width="1.6" fill="none"/></svg></div>

  <div class="abs main-nav"></div>
  <nav class="abs nav-links">
    <span class="active">ABOUT US</span>
    <span>STORE LOCATION</span>
    <span>REPAIR</span>
    <span style="padding-left:60px">CONTACT US</span>
    <span>LOG IN</span>
    <span>REGISTER</span>
  </nav>
  <div class="abs social-top"><i></i><i></i><i></i><i></i><i></i><i></i></div>

  <div class="abs cat-bar"></div>
  <nav class="abs cat-links">
    <span>PRODUCTION GLASS</span><b>|</b>
    <span>APPAREL</span><b>|</b>
    <span>ACCESSORIES</span><b>|</b>
    <span>HEADY GLASS</span>
  </nav>
  <div class="abs search"><span>Search product here</span><i><svg width="14" height="14" viewBox="0 0 14 14"><circle cx="6" cy="6" r="4.5" stroke="#fff" stroke-width="2" fill="none"/><path d="M9 9 13 13" stroke="#fff" stroke-width="2"/></svg></i></div>
</header>

<section class="hero">
  <div class="abs hero-img" role="img" aria-label="Smiling family carrying wrapped gift boxes outdoors"></div>
  <div class="abs slide-arrow" style="left:132px;top:393px"><svg width="9" height="14" viewBox="0 0 9 14"><path d="M8 1 2 7 8 13" stroke="#fff" stroke-width="2" fill="none"/></svg></div>
  <div class="abs slide-arrow" style="left:760px;top:393px"><svg width="9" height="14" viewBox="0 0 9 14"><path d="M1 1 7 7 1 13" stroke="#fff" stroke-width="2" fill="none"/></svg></div>
  <div class="abs dots"><i class="on"></i><i></i><i></i><i></i></div>

  <aside class="abs perks">
    <div class="perk" style="top:20px;height:100px;padding-top:18px">
      <svg width="36" height="22" viewBox="0 0 36 22"><rect x="0" y="2" width="22" height="14" fill="#fff"/><path d="M22 6H30L35 11V16H22Z" fill="#fff"/><circle cx="7" cy="18" r="3.5" fill="#fff" stroke="#d0222a" stroke-width="2"/><circle cx="28" cy="18" r="3.5" fill="#fff" stroke="#d0222a" stroke-width="2"/></svg>
      <h4>FREE USA SHIPPING</h4><p>Speedy deliveries, ships from the USA</p>
    </div>
    <div class="perk dark" style="top:126px;height:130px;padding-top:36px">
      <svg width="26" height="28" viewBox="0 0 26 28"><path d="M13 1 24 5V13C24 20 19 25 13 27 7 25 2 20 2 13V5Z" stroke="#fff" stroke-width="2" fill="none"/><path d="M8 14 12 18 19 10" stroke="#fff" stroke-width="2" fill="none"/></svg>
      <h4>SATISFACTION GUARANTEED</h4><p>Thousands of happy customers</p>
    </div>
    <div class="perk" style="top:266px;height:120px;padding-top:22px">
      <svg width="28" height="28" viewBox="0 0 28 28"><circle cx="14" cy="14" r="12" stroke="#fff" stroke-width="2" fill="none"/><text x="14" y="18" text-anchor="middle" font-family="Open Sans,Arial,sans-serif" font-size="10" font-weight="700" fill="#fff">24</text></svg>
      <h4>GREAT CUSTOMER SERVICE</h4><p>Fast and friendly responses</p>
    </div>
  </aside>
</section>

<div class="abs grey-area"></div>

<!-- bag collection -->
<section>
  <div class="abs tag" style="top:652px">BAG COLLECTION:</div>
  <div class="abs panel" style="top:691px"></div>
  <div class="abs thumb" style="left:143px;top:708px"><div role="img" aria-label="Magenta leather handbag" style="background:linear-gradient(#c43a8f,#8e1f64)"></div></div>
  <div class="abs thumb" style="left:320px;top:708px"><div role="img" aria-label="Coral tote bag" style="background:linear-gradient(#f07a7a,#d9474d)"></div></div>
  <div class="abs thumb sel" style="left:485px;top:708px"><div role="img" aria-label="Tan leather satchel" style="background:linear-gradient(#d08a48,#8b4d1f)"></div></div>
  <div class="abs pointer" style="left:638px;top:768px"></div>
  <div class="abs thumb" style="left:143px;top:875px"><div role="img" aria-label="Olive canvas messenger bag" style="background:linear-gradient(#7a7a64,#4f4f3e)"></div></div>
  <div class="abs thumb" style="left:320px;top:875px"><div role="img" aria-label="Black laptop sleeve bag" style="background:linear-gradient(#3a3a3a,#0f0f0f)"></div></div>
  <div class="abs thumb" style="left:485px;top:875px"><div role="img" aria-label="Brown leather briefcase" style="background:linear-gradient(#8a4a2a,#4d2412)"></div></div>
  <div class="abs loadbar" style="left:210px;top:1053px"><i></i>Load more</div>
  <div class="abs radio" style="left:398px;top:1066px"><b></b>Men</div>
  <div class="abs radio on" style="left:495px;top:1066px"><b></b>Women</div>
  <div class="abs feature" style="left:676px;top:708px">
    <div role="img" aria-label="Assortment of messenger and shoulder bags" style="width:100%;height:100%;background:linear-gradient(#d9d9d9,#8a8a8a 60%,#3c3c3c)"></div>
    <div class="abs price-bar"><span class="price">$50</span>
      <svg class="abs" style="left:84px;top:34px" width="22" height="20" viewBox="0 0 22 20"><path d="M11 19 2 10C-1 6 2 1 6 1 8.5 1 10 3 11 4 12 3 13.5 1 16 1 20 1 23 6 20 10Z" fill="#d0222a"/></svg>
      <svg class="abs" style="left:310px;top:50px" width="30" height="26" viewBox="0 0 30 26"><path d="M1 2H6L9 16H25L28 6H8" stroke="#fff" stroke-width="2.4" fill="none"/><circle cx="11" cy="22" r="2.5" fill="#fff"/><circle cx="23" cy="22" r="2.5" fill="#fff"/></svg>
    </div>
  </div>
</section>

<!-- shoes collection -->
<section>
  <div class="abs tag" style="top:1168px">SHOES COLLECTIONS:</div>
  <div class="abs panel" style="top:1207px"></div>
  <div class="abs thumb" style="left:143px;top:1224px"><div role="img" aria-label="White printed t-shirt" style="background:linear-gradient(#f2f2f2,#9a9a9a)"></div></div>
  <div class="abs thumb" style="left:320px;top:1224px"><div role="img" aria-label="Striped high-top sneakers" style="background:linear-gradient(#d64040,#3a7bbf)"></div></div>
  <div class="abs thumb sel" style="left:485px;top:1224px"><div role="img" aria-label="White and red running shoe" style="background:linear-gradient(#eeeeee,#9c2a2a)"></div></div>
  <div class="abs pointer" style="left:638px;top:1284px"></div>
  <div class="abs thumb" style="left:143px;top:1391px"><div role="img" aria-label="Red and gold basketball shoe" style="background:linear-gradient(#c62b2b,#d3a43a)"></div></div>
  <div class="abs thumb" style="left:320px;top:1391px"><div role="img" aria-label="Grey trail running shoe" style="background:linear-gradient(#e4e4e4,#5a5a5a)"></div></div>
  <div class="abs thumb" style="left:485px;top:1391px"><div role="img" aria-label="Burgundy canvas sneaker" style="background:linear-gradient(#b84040,#6e1c1c)"></div></div>
  <div class="abs loadbar" style="left:210px;top:1568px"><i></i>Load more</div>
  <div class="abs radio" style="left:398px;top:1581px"><b></b>Men</div>
  <div class="abs radio on" style="left:495px;top:1581px"><b></b>Women</div>
  <div class="abs feature" style="left:676px;top:1224px">
    <div role="img" aria-label="Close-up of white and red running shoe" style="width:100%;height:100%;background:linear-gradient(#6a6a6a,#d9d9d9 55%,#a53b3b 80%,#2a2a2a)"></div>
    <div class="abs price-bar" style="background:none"><span class="price">$50</span>
      <svg class="abs" style="left:84px;top:34px" width="22" height="20" viewBox="0 0 22 20"><path d="M11 19 2 10C-1 6 2 1 6 1 8.5 1 10 3 11 4 12 3 13.5 1 16 1 20 1 23 6 20 10Z" fill="#d0222a"/></svg>
      <svg class="abs" style="left:310px;top:50px" width="30" height="26" viewBox="0 0 30 26"><path d="M1 2H6L9 16H25L28 6H8" stroke="#fff" stroke-width="2.4" fill="none"/><circle cx="11" cy="22" r="2.5" fill="#fff"/><circle cx="23" cy="22" r="2.5" fill="#fff"/></svg>
    </div>
  </div>
</section>

<!-- latest products -->
<section>
  <div class="abs latest"></div>
  <div class="abs tabs"><span class="on">LATEST ▾</span><span>FEATURES ▾</span><span>POPULAR ▾</span></div>
  <div class="abs slide-arrow" style="left:150px;top:1848px"><svg width="9" height="14" viewBox="0 0 9 14"><path d="M8 1 2 7 8 13" stroke="#fff" stroke-width="2" fill="none"/></svg></div>
  <div class="abs slide-arrow" style="left:1020px;top:1848px"><svg width="9" height="14" viewBox="0 0 9 14"><path d="M1 1 7 7 1 13" stroke="#fff" stroke-width="2" fill="none"/></svg></div>

  <div class="abs card" style="left:202px" role="img" aria-label="Model wearing orange top"><div style="width:100%;height:100%;background:linear-gradient(#c9c0b8,#e8643c)"></div><div class="label red"><small>CONSECTETUR</small><em>★★★★</em><strong>$70</strong></div></div>
  <div class="abs card" style="left:364px" role="img" aria-label="Grey graphic t-shirt"><div style="width:100%;height:100%;background:linear-gradient(#d9d9d9,#6d6d6d)"></div><div class="label"><small>CONSECTETUR</small><em>★★★★</em><strong>$70</strong></div></div>
  <div class="abs card" style="left:524px" role="img" aria-label="Model wearing black printed t-shirt"><div style="width:100%;height:100%;background:linear-gradient(#e4e4e4,#1d1d1d)"></div><div class="label"><small>CONSECTETUR</small><em>★★★★</em><strong>$70</strong></div></div>
  <div class="abs card" style="left:684px" role="img" aria-label="Model wearing taupe v-neck t-shirt"><div style="width:100%;height:100%;background:linear-gradient(#dedede,#8e7d70)"></div><div class="label"><small>CONSECTETUR</small><em>★★★★</em><strong>$70</strong></div></div>
  <div class="abs card" style="left:844px" role="img" aria-label="Model wearing teal t-shirt"><div style="width:100%;height:100%;background:linear-gradient(#e0e0e0,#3e8fa8)"></div><div class="label"><small>CONSECTETUR</small><em>★★★★</em><strong>$70</strong></div></div>
</section>

<footer>
  <div class="abs foot-col" style="left:86px;top:2122px">
    <h5>CATEGORY</h5>
    <ul><li>PRODUCTION GLASS</li><li>APPAREL</li><li>ACCESSORIES</li><li>HEADY GLASS</li></ul>
  </div>
  <div class="abs foot-col" style="left:278px;top:2122px">
    <h5>INFORMATION</h5>
    <ul><li>ABOUT US</li><li>CONTACT US</li><li>FAQ</li><li>FORMS OF PAYMENT</li><li>INSTRUCTIONS</li><li>PRIVACY POLICY</li></ul>
  </div>
  <div class="abs foot-col" style="left:418px;top:2160px">
    <ul style="margin-top:0"><li>REPAIR SERVICE</li><li>TERMS OF SERVICES</li><li>SITE MAP</li></ul>
  </div>
  <div class="abs foot-col" style="left:598px;top:2122px"><h5>NEWSLETTER</h5></div>
  <div class="abs news-input">Email ADDress</div>
  <div class="abs subscribe">Subscribe</div>
  <p class="abs news-note">We ensure your adresss will be secure</p>

  <div class="abs foot-col" style="left:841px;top:2122px"><h5>ADDRESS</h5></div>
  <div class="abs addr-row" style="top:2164px"><i></i><span>sitam, quis nostrud exercitation<br>ullamco laboris nisi ut<br>aliquip ex ea</span></div>
  <div class="abs addr-row" style="top:2228px"><i></i><span class="em">anymail@mailbay.com</span></div>
  <div class="abs addr-row" style="top:2264px"><i></i><span>+16541 5200 7431</span></div>

  <div class="abs social-foot"><i></i><i></i><i></i><i></i></div>
  <p class="abs copyright">@Copyright by &nbsp;2015 with company Holder</p>
</footer>

</body>
</html>
```